business card for glass company

logo on business card and letterhead. our business is installing and servicing glass and mirror in commercial and industrial buildings in the Toronto area. full company name, Halworth Glass and Mirror Ltd.
i am looking for a business card and letterhead design.
on the letterhead i need company name and contact info
Halworth Glass and Mirror Ltd.
718 Larchmere Rd.
Toronto, Ontario
M4K 7B9
on the cards the contact info is
Dana Halworth
718 Larchmere Rd.
Toronto, Ontario
M4K 7B9
(416) 555-0142
(416) 555 0187-cell
i need another card with different name
Martin Quell
594 Kemble St. N
Hamilton Ontario
L3R 9T2
(416) 555-0142
(416) 555-0163
Target Market(s)
Professionals in industrial and commercial building construction, architects, general contractors, building managers and owners.
Industry/Entity Type
Business
Requirements
Must have
- simple design with two colors. emphasis on the name Halworth.

```html
<!DOCTYPE html>
<html lang="en">
<head>
<meta charset="utf-8">
<title>Halworth Glass and Mirror Ltd. — Business Cards and Letterhead</title>
<link rel="stylesheet" href="https://fonts.googleapis.com/css2?family=Noto+Sans:wght@700&display=swap">
<style>
  :root {
    --navy: #00234f;
    --sky: #0089cf;
    --ink: #12305c;
    --paper: #ffffff;
    --edge: #3a3a3a;
  }
  html, body {
    margin: 0;
    padding: 0;
    width: 1200px;
    height: 925px;
    overflow: hidden;
    background: var(--paper);
  }
  .sheet {
    display: block;
    width: 1200px;
    height: 925px;
  }
  .sheet text {
    font-family: "Noto Sans", "DejaVu Sans", Verdana, sans-serif;
    font-weight: 700;
  }
  .trim { fill: var(--paper); stroke: var(--edge); stroke-width: 0.8; }
  .panel { fill: var(--navy); }
  .tab { fill: var(--sky); }
  .company-name { fill: var(--paper); letter-spacing: 0.3px; }
  .person-name { fill: var(--paper); }
  .contact { fill: var(--ink); }
  .letter-address { fill: var(--paper); }
</style>
</head>
<body>
<svg class="sheet" viewBox="0 0 747 576" xmlns="http://www.w3.org/2000/svg" role="img" aria-label="Business cards and letterhead for Halworth Glass and Mirror Ltd.">
  <defs>
    <clipPath id="card-one-clip"><rect x="0.5" y="0.5" width="413" height="272"/></clipPath>
    <clipPath id="card-two-clip"><rect x="5" y="302.5" width="413" height="272"/></clipPath>
    <clipPath id="letterhead-clip"><rect x="449.5" y="5.5" width="296.5" height="569"/></clipPath>
  </defs>

  <!-- Business card: Dana Halworth -->
  <g class="card card-dana">
    <rect class="trim" x="0.5" y="0.5" width="413" height="272"/>
    <g clip-path="url(#card-one-clip)">
      <rect class="panel" x="3" y="10" width="350" height="200" rx="13"/>
      <rect class="tab" x="362" y="10" width="80" height="200" rx="13"/>
    </g>
    <text class="company-name" x="8" y="52" font-size="16.5" textLength="338" lengthAdjust="spacingAndGlyphs">HALWORTH GLASS AND MIRROR LTD.</text>
    <text class="person-name" x="8" y="199" font-size="18.5">DANA HALWORTH</text>
    <text class="contact" x="8" y="229" font-size="12.5">718 Larchmere Rd.Toronto, Ontario, M4K 7B9</text>
    <text class="contact" x="8" y="246" font-size="12.5">(416) 555-0142</text>
    <text class="contact" x="8" y="263" font-size="12.5">(416) 555 0187-cell</text>
  </g>

  <!-- Business card: Martin Quell -->
  <g class="card card-martin">
    <rect class="trim" x="5" y="302.5" width="413" height="272"/>
    <g clip-path="url(#card-two-clip)">
      <rect class="panel" x="5" y="312" width="352" height="200" rx="13"/>
      <rect class="tab" x="366" y="312" width="80" height="200" rx="13"/>
    </g>
    <text class="company-name" x="12" y="354" font-size="16.5" textLength="338" lengthAdjust="spacingAndGlyphs">HALWORTH GLASS AND MIRROR LTD.</text>
    <text class="person-name" x="12" y="501" font-size="18.5">MARTIN QUELL</text>
    <text class="contact" x="12" y="531" font-size="12.5">594 Kemble St. N,Hamilton Ontario, L3R 9T2</text>
    <text class="contact" x="12" y="548" font-size="12.5">(416) 555-0142</text>
    <text class="contact" x="12" y="565" font-size="12.5">(416) 555-0163</text>
  </g>

  <!-- Letterhead -->
  <g class="letterhead">
    <rect class="trim" x="449.5" y="5.5" width="296.5" height="569"/>
    <g clip-path="url(#letterhead-clip)">
      <rect class="panel" x="451" y="26" width="216" height="110" rx="11"/>
      <rect class="tab" x="676" y="28" width="90" height="108" rx="11"/>
    </g>
    <text class="company-name" x="461" y="56" font-size="10" textLength="194" lengthAdjust="spacingAndGlyphs">HALWORTH GLASS AND MIRROR LTD.</text>
    <text class="letter-address" x="459" y="126" font-size="7.2">718 Larchmere Rd. Toronto, Ontario M4K 7B9</text>
  </g>
</svg>
</body>
</html>
```